Party Favors and Decorations Business Needs A Business Card Design

We are in need of a Logo design and business card design for a new small business called Willow Bay Designs. We create party decorations and favours for Bridal Showers, Baby Showers, Weddings Birthdays etc. This is a very personalized service based on Clients theme, colour, and style. We are looking for a high end elegant look. I have attached a file to the style I like including the type of paper.

Target Market(s)

women, young adults, expectant mothers, mothers

Industry/Entity Type

Small Business

Contact Information for Business Card

Willow Bay Designs Essex, ON 519-806-4192 willowbaydesigns-example.ca danielle@willowbaygiftwrap-example.com find us on Friendlink

Logo Text

Willow Bay Designs

Font styles to use
Script

Requirements
Must have
• Name, email, web address, phone number
Should not have
• cutesy graphics

```html
<!DOCTYPE html>
<html lang="en">
<head>
<meta charset="utf-8">
<title>Willow Bay Designs — Business Card</title>
<link rel="stylesheet" href="https://fonts.googleapis.com/css2?family=Open+Sans:wght@400;600&display=swap">
<style>
  :root {
    --stage: #3a322b;
    --card: #050505;
    --ink: #f4f4f4;
    --ink-soft: #d9d9d9;
  }
  html, body {
    margin: 0;
    padding: 0;
    overflow: hidden;
  }
  body {
    width: 1200px;
    height: 885px;
    background: var(--stage);
    position: relative;
    font-family: "Open Sans", Arial, sans-serif;
    color: var(--ink);
  }
  .card {
    position: absolute;
    width: 560px;
    height: 320px;
    background: var(--card);
    border-radius: 18px;
    box-shadow: 0 10px 30px rgba(0,0,0,0.45);
    overflow: hidden;
  }
  .card--front { left: 40px; top: 100px; }
  .card--back  { left: 600px; top: 465px; }

  .brand-name {
    position: absolute;
    font-family: "Open Sans", Arial, sans-serif;
    font-weight: 400;
    color: var(--ink);
    letter-spacing: 0.5px;
    white-space: nowrap;
  }
  .card--front .brand-name {
    left: 40px;
    top: 58px;
    font-size: 30px;
  }
  .card--back .brand-name {
    left: 0;
    right: 0;
    top: 136px;
    text-align: center;
    font-size: 40px;
  }

  .employee-name {
    position: absolute;
    right: 40px;
    top: 70px;
    font-size: 22px;
    font-weight: 600;
  }
  .name-rule {
    position: absolute;
    left: 40px;
    right: 40px;
    top: 112px;
    height: 1px;
    background: var(--ink-soft);
  }

  .contact-list {
    position: absolute;
    left: 40px;
    bottom: 36px;
    margin: 0;
    padding: 0;
    list-style: none;
    font-size: 13.5px;
    line-height: 26px;
  }
  .contact-list li {
    display: flex;
    align-items: center;
    gap: 9px;
  }
  .contact-icon {
    width: 17px;
    height: 17px;
    flex: none;
  }

  .social {
    position: absolute;
    right: 40px;
    bottom: 40px;
    display: flex;
    align-items: center;
    gap: 9px;
  }
  .social-square {
    width: 30px;
    height: 30px;
    background: var(--ink);
    border-radius: 3px;
  }
  .social-text {
    font-size: 12px;
    line-height: 1.1;
  }
  .social-text strong {
    display: block;
    font-size: 20px;
    font-weight: 600;
  }
</style>
</head>
<body>

<section class="card card--front" aria-label="Business card front">
  <div class="brand-name">Willow Bay Designs</div>
  <div class="employee-name">Employee Name</div>
  <div class="name-rule"></div>

  <ul class="contact-list">
    <li>
      <svg class="contact-icon" viewBox="0 0 18 18" aria-hidden="true">
        <rect width="18" height="18" rx="4" fill="#f4f4f4"/>
        <path d="M5.2 4.2l2 0.2 0.8 2.4-1.2 1a6 6 0 0 0 3.4 3.4l1-1.2 2.4 0.8 0.2 2c-4.6 0.6-9.2-4-8.6-8.6z" fill="#050505"/>
      </svg>
      519-806-4192
    </li>
    <li>
      <svg class="contact-icon" viewBox="0 0 18 18" aria-hidden="true">
        <rect width="18" height="18" rx="4" fill="#f4f4f4"/>
        <g fill="none" stroke="#050505" stroke-width="1.1">
          <circle cx="9" cy="9" r="5"/>
          <ellipse cx="9" cy="9" rx="2.2" ry="5"/>
          <line x1="4" y1="9" x2="14" y2="9"/>
        </g>
      </svg>
      willowbaydesigns-example.ca
    </li>
    <li>
      <svg class="contact-icon" viewBox="0 0 18 18" aria-hidden="true">
        <rect width="18" height="18" rx="4" fill="#f4f4f4"/>
        <g fill="none" stroke="#050505" stroke-width="1.1">
          <rect x="4" y="5.5" width="10" height="7"/>
          <polyline points="4,5.5 9,9.5 14,5.5"/>
        </g>
      </svg>
      danielle@willowbaygiftwrap-example.com
    </li>
  </ul>

  <div class="social">
    <div class="social-square" aria-hidden="true"></div>
    <div class="social-text">Find us on<strong>Friendlink</strong></div>
  </div>
</section>

<section class="card card--back" aria-label="Business card back">
  <div class="brand-name">Willow Bay Designs</div>
</section>

</body>
</html>
```